Graphic Design Set for Banner Ads - Sizes and Specs for Pixmora

We need a set of 6 ads of the following sizes created for Pixmora:

Medium rectangle: 300×250
Leaderboard: 728×90
Wide skyscraper: 160×600
Large rectangle: 300x600
Mobile leaderboard: 320×50

Here are the Formatting Guidelines (WEB ADS): https://help.pixmora.example/hc/en-us/articles/583920147-Ad-Content-and-Format-Guidelines

Here is the website: https://valmiraliving.example/

Here are some words for the ad - feel free to use creative liberties if you have something better or need less words.

1. The Future of Aging is Here

2. Dementia At-Home Care

3. Benefits of an Assisted Living from the Privacy of Your Home - link to

4. Idaho's New Senior Care Option

5. The Security of Senior Living from the Comfort of Your Home

I have the images for all website photos, if you need more images, please let me know.

Target Market(s)

Women age 55+

Industry/Entity Type

Graphic Design

Requirements
Must have
• Incorporate website imagery as much as possible
Should not have
• a feeling of helplessness, old, etc.

```html
<!DOCTYPE html>
<html lang="en">
<head>
<meta charset="utf-8">
<title>Valmira Living — Banner Ad Set</title>
<link rel="stylesheet" href="https://fonts.googleapis.com/css2?family=Inter:wght@300;400&display=swap">
<style>
  :root {
    --stage: #2b2b2b;
    --paper: #ffffff;
    --ink: #141414;
    --gold: #c9a23c;
    --gold-light: #e6cc7a;
    --button: #0b0b0b;
    --button-text: #ffffff;
  }
  * { box-sizing: border-box; margin: 0; padding: 0; }
  html, body { width: 1200px; height: 1200px; overflow: hidden; }
  body {
    background: var(--stage);
    font-family: "Inter", Helvetica, Arial, sans-serif;
    color: var(--ink);
    position: relative;
  }
  .ad {
    position: absolute;
    background: var(--paper);
    overflow: hidden;
    box-shadow: 0 6px 18px rgba(0,0,0,.45);
  }
  .brand {
    position: absolute;
    font-weight: 400;
    color: var(--ink);
    letter-spacing: .02em;
    line-height: 1;
    white-space: nowrap;
  }
  .headline {
    position: absolute;
    font-weight: 300;
    color: var(--ink);
    line-height: 1.08;
  }
  .rule { position: absolute; background: var(--gold); }
  .photo { position: absolute; inset: 0; }
  .wedge { position: absolute; inset: 0; width: 100%; height: 100%; }
  .cta {
    position: absolute;
    background: var(--button);
    color: var(--button-text);
    font-weight: 400;
    display: flex; align-items: center; justify-content: center;
    outline: 1px solid rgba(255,255,255,.8);
    outline-offset: 3px;
    white-space: nowrap;
  }

  /* Wide skyscraper */
  .ad-skyscraper { left: 90px; top: 54px; width: 170px; height: 634px; }
  .ad-skyscraper .brand { left: 18px; top: 30px; font-size: 19px; }
  .ad-skyscraper .rule { left: 18px; top: 105px; width: 136px; height: 2px; }
  .ad-skyscraper .headline { left: 19px; top: 120px; font-size: 20px; }
  .ad-skyscraper .photo {
    clip-path: polygon(0 270px, 100% 200px, 100% 100%, 0 100%);
    background: linear-gradient(180deg, #d9dcd8 30%, #3f5a3c 48%, #9aa3a6 60%, #d7b7b9 75%, #b8a88e 100%);
  }
  .ad-skyscraper .cta { left: 33px; top: 582px; width: 104px; height: 31px; font-size: 14px; }

  /* Medium rectangle */
  .ad-medium { left: 348px; top: 529px; width: 352px; height: 291px; }
  .ad-medium .brand { left: 12px; top: 26px; font-size: 15px; }
  .ad-medium .rule { left: 130px; top: 10px; width: 1px; height: 52px; }
  .ad-medium .headline { left: 141px; top: 23px; font-size: 16px; font-weight: 400; }
  .ad-medium .photo {
    clip-path: polygon(0 85px, 100% 60px, 100% 100%, 0 100%);
    background: radial-gradient(ellipse at 50% 35%, #f0a03a 0%, #b8481c 30%, #3a1c12 65%, #1a120c 100%);
  }
  .ad-medium .cta { left: 231px; top: 239px; width: 94px; height: 30px; font-size: 13px; }

  /* Large rectangle */
  .ad-large { left: 794px; top: 184px; width: 318px; height: 636px; }
  .ad-large .brand { left: 21px; top: 52px; font-size: 30px; }
  .ad-large .rule { left: 21px; top: 120px; width: 273px; height: 2px; }
  .ad-large .headline { left: 21px; top: 135px; font-size: 21px; }
  .ad-large .photo {
    clip-path: polygon(0 265px, 100% 200px, 100% 100%, 0 100%);
    background: linear-gradient(160deg, #4d6b3b 0%, #7b8a62 35%, #a09a90 60%, #e8e1d6 85%, #d9cfc1 100%);
  }
  .ad-large .cta { left: 104px; top: 579px; width: 112px; height: 32px; font-size: 14px; }

  /* Mobile leaderboard */
  .ad-mobile { left: 44px; top: 864px; width: 374px; height: 58px; }
  .ad-mobile .brand { left: 10px; top: 22px; font-size: 14px; }
  .ad-mobile .rule { left: 115px; top: 8px; width: 1px; height: 42px; }
  .ad-mobile .headline { left: 132px; top: 7px; font-size: 9.5px; font-weight: 400; line-height: 1.05; }
  .ad-mobile .photo {
    clip-path: polygon(218px 0, 100% 0, 100% 100%, 198px 100%);
    background: linear-gradient(90deg, #dfe4de 0%, #c8cbc4 55%, #4a4f52 80%, #2b2f33 100%);
  }
  .ad-mobile .cta { left: 132px; top: 41px; width: 46px; height: 10px; font-size: 6px; outline: none; }

  /* Leaderboard */
  .ad-leaderboard { left: 262px; top: 1010px; width: 872px; height: 107px; }
  .ad-leaderboard .brand { left: 22px; top: 40px; font-size: 28px; }
  .ad-leaderboard .rule { left: 229px; top: 18px; width: 1px; height: 74px; }
  .ad-leaderboard .headline { left: 259px; top: 24px; font-size: 21px; }
  .ad-leaderboard .photo {
    clip-path: polygon(545px 0, 100% 0, 100% 100%, 510px 100%);
    background: linear-gradient(90deg, #e6ebe2 0%, #d6dbd2 55%, #6a6c6a 78%, #2e3236 100%);
  }
  .ad-leaderboard .cta { left: 551px; top: 62px; width: 84px; height: 26px; font-size: 12px; }
</style>
</head>
<body>

<!-- Wide skyscraper 160×600 -->
<section class="ad ad-skyscraper" aria-label="Wide skyscraper ad">
  <div class="brand">Valmira Living</div>
  <div class="rule"></div>
  <h2 class="headline">Idaho's New<br>Senior Care<br>Option</h2>
  <div class="photo" role="img" aria-label="Active senior woman stretching on a yoga mat by a lake"></div>
  <svg class="wedge" viewBox="0 0 170 634" preserveAspectRatio="none" aria-hidden="true">
    <defs><linearGradient id="g1" x1="0" x2="1"><stop offset="0" stop-color="#b88a22"/><stop offset=".6" stop-color="#e6cc7a"/><stop offset="1" stop-color="#c9a23c"/></linearGradient></defs>
    <polygon points="0,258 170,200 170,206 0,285" fill="url(#g1)"/>
  </svg>
  <a class="cta">Learn More</a>
</section>

<!-- Medium rectangle 300×250 -->
<section class="ad ad-medium" aria-label="Medium rectangle ad">
  <div class="brand">Valmira Living</div>
  <div class="rule"></div>
  <h2 class="headline">The Future of Aging is Here</h2>
  <div class="photo" role="img" aria-label="Feet in cosy knitted socks resting before a fireplace with wine glasses"></div>
  <svg class="wedge" viewBox="0 0 352 291" preserveAspectRatio="none" aria-hidden="true">
    <defs><linearGradient id="g2" x1="0" x2="1"><stop offset="0" stop-color="#b88a22"/><stop offset=".6" stop-color="#e6cc7a"/><stop offset="1" stop-color="#c9a23c"/></linearGradient></defs>
    <polygon points="0,72 352,60 352,62 0,85" fill="url(#g2)"/>
  </svg>
  <a class="cta">Learn More</a>
</section>

<!-- Large rectangle 300×600 -->
<section class="ad ad-large" aria-label="Large rectangle ad">
  <div class="brand">Valmira Living</div>
  <div class="rule"></div>
  <h2 class="headline">The Security of Senior Living<br>from the Comfort of<br>Your Home</h2>
  <div class="photo" role="img" aria-label="Smiling senior woman in a garden chair beside a white poodle"></div>
  <svg class="wedge" viewBox="0 0 318 636" preserveAspectRatio="none" aria-hidden="true">
    <defs><linearGradient id="g3" x1="0" x2="1"><stop offset="0" stop-color="#b88a22"/><stop offset=".6" stop-color="#e6cc7a"/><stop offset="1" stop-color="#c9a23c"/></linearGradient></defs>
    <polygon points="0,245 318,200 318,206 0,266" fill="url(#g3)"/>
  </svg>
  <a class="cta">Learn More</a>
</section>

<!-- Mobile leaderboard 320×50 -->
<section class="ad ad-mobile" aria-label="Mobile leaderboard ad">
  <div class="brand">Valmira Living</div>
  <div class="rule"></div>
  <h2 class="headline">Dementia<br>At-Home<br>Care</h2>
  <div class="photo" role="img" aria-label="Portrait of a senior man in a sweater"></div>
  <svg class="wedge" viewBox="0 0 374 58" preserveAspectRatio="none" aria-hidden="true">
    <defs><linearGradient id="g4" x1="0" x2="1"><stop offset="0" stop-color="#b88a22"/><stop offset="1" stop-color="#e6cc7a"/></linearGradient></defs>
    <polygon points="211,0 218,0 198,58 190,58" fill="url(#g4)"/>
  </svg>
  <a class="cta">Learn More</a>
</section>

<!-- Leaderboard 728×90 -->
<section class="ad ad-leaderboard" aria-label="Leaderboard ad">
  <div class="brand">Valmira Living</div>
  <div class="rule"></div>
  <h2 class="headline">Benefits of an Assisted<br>Living from the Privacy<br>of Your Home</h2>
  <div class="photo" role="img" aria-label="Portrait of a senior man resting his arms on a table"></div>
  <svg class="wedge" viewBox="0 0 872 107" preserveAspectRatio="none" aria-hidden="true">
    <defs><linearGradient id="g5" x1="0" x2="1"><stop offset="0" stop-color="#b88a22"/><stop offset="1" stop-color="#e6cc7a"/></linearGradient></defs>
    <polygon points="535,0 545,0 510,107 495,107" fill="url(#g5)"/>
  </svg>
  <a class="cta">Learn More</a>
</section>

</body>
</html>
```